RW Hollis LLC Business Card - Civil Engineering & Consulting Firm

We need a Business Card that is elegant, and masculine.  It is our Professional Civil Engineering & Consulting Company located in San Antonio TX (Not s construction or builder firm- no gears & no tool images please). We provide civil engineering services including  commercial site plans, grading and drainage plans, utility plans, hydraulics and hydrology, land planning, utility coordination, and other general civil engineering services related to commercial and residential development.
We have 2 existing Logos. We would like to convey reliability, strength, trustworthiness and attention to detail.  Blues and orange tones as per logo We are OK with the use of a darker blue in the mix.  We have 2 logo versions - Full Company Name Logo to go on the back of card, & Small Icon Logo for the front w/ personal Info.

Target Market(s)
Architects, Real Estate Developers, Other Strctural Engineers, Surveyers, General Contractors
Industry/Entity Type
Professional Civil Engineering
Contact Information for Business Card
Name, Position, Address, Cell & Office #, email, and company website
Font styles to use
Other font styles liked:
- Avian
Requirements
Should not have
- No Tools, No Gears, no Cranes, or Construction Equipment.

```html
<!DOCTYPE html>
<html lang="en">
<head>
<meta charset="utf-8">
<title>RW Hollis LLC — Business Card</title>
<link rel="stylesheet" href="https://fonts.googleapis.com/css2?family=Michroma&family=Questrial&family=Raleway:wght@300;400;700&display=swap">
<style>
  :root {
    --bg: #c8c9c8;
    --card: #000000;
    --panel: #222222;
    --blue: #7aaedb;
    --orange: #ef922d;
    --white: #ffffff;
    --soft: #c9c9c9;
  }
  * { margin: 0; padding: 0; box-sizing: border-box; }
  html, body {
    width: 1200px; height: 1200px; overflow: hidden;
    background: var(--bg);
  }
  .canvas { position: relative; width: 1200px; height: 1200px; }

  .card {
    position: absolute; left: 178px; width: 869px; height: 509px;
    background: var(--card); overflow: hidden;
  }
  .card--back { top: 71px; }
  .card--front { top: 615px; }

  /* Back: company name lockup */
  .company {
    position: absolute; left: 0; right: 0; top: 118px;
    text-align: center;
  }
  .company__name {
    font-family: "Michroma", sans-serif;
    font-size: 72px; letter-spacing: 4px;
    color: var(--blue); line-height: 1;
  }
  .company__rule {
    position: absolute; left: 233px; width: 530px; top: 264px; height: 2px;
    background: var(--blue);
  }
  .company__tagline {
    position: absolute; left: 0; right: 0; top: 286px;
    text-align: center;
    font-family: "Questrial", sans-serif;
    font-size: 24px; letter-spacing: 6.4px;
    color: var(--orange);
  }

  .web-band {
    position: absolute; left: 0; right: 0; top: 413px; height: 44px;
    display: flex;
  }
  .web-band__accent { width: 231px; background: var(--orange); position: relative; }
  .web-band__icon { position: absolute; right: 4px; top: 9px; width: 26px; height: 26px; }
  .web-band__url {
    flex: 1; background: var(--blue);
    font-family: "Raleway", sans-serif; font-weight: 400;
    font-size: 27px; letter-spacing: 0.5px;
    color: #111; line-height: 44px; padding-left: 30px;
  }
  .web-band__url strong { font-weight: 700; }

  /* Front: personal details */
  .front__brand {
    position: absolute; left: 0; top: 0; width: 276px; height: 509px;
    display: flex; align-items: center; justify-content: center;
  }
  .front__brand-name {
    font-family: "Michroma", sans-serif;
    font-size: 52px; letter-spacing: 4px; color: var(--blue);
    writing-mode: vertical-rl; transform: rotate(180deg);
    white-space: nowrap;
  }
  .divider-blue { position: absolute; left: 271px; top: 0; width: 11px; height: 320px; background: var(--blue); }
  .divider-orange { position: absolute; left: 271px; top: 320px; width: 11px; height: 189px; background: var(--orange); }
  .details-panel { position: absolute; left: 282px; right: 0; top: 320px; bottom: 0; background: var(--panel); }

  .person {
    position: absolute; right: 51px; top: 215px; text-align: right;
  }
  .person__name {
    font-family: "Michroma", sans-serif;
    font-size: 27px; letter-spacing: 4px; color: var(--blue);
    line-height: 1.2;
  }
  .person__name span { color: var(--orange); }
  .person__position {
    font-family: "Raleway", sans-serif; font-weight: 400;
    font-size: 23px; letter-spacing: 1px; color: var(--white);
    margin-top: 4px;
  }

  .contact {
    position: absolute; left: 375px; top: 336px;
    list-style: none;
    font-family: "Raleway", sans-serif; font-weight: 300;
    font-size: 22px; line-height: 33px; color: var(--soft);
  }
  .contact__label { color: var(--orange); font-weight: 700; }
</style>
</head>
<body>
<div class="canvas">

  <section class="card card--back" aria-label="Card back">
    <div class="company">
      <div class="company__name">RW HOLLIS LLC</div>
    </div>
    <div class="company__rule"></div>
    <div class="company__tagline">CONSULTING ENGINEERS</div>

    <div class="web-band">
      <div class="web-band__accent">
        <svg class="web-band__icon" viewBox="0 0 26 26" aria-hidden="true">
          <circle cx="13" cy="13" r="11" fill="none" stroke="#111" stroke-width="2"/>
          <ellipse cx="13" cy="13" rx="5" ry="11" fill="none" stroke="#111" stroke-width="1.8"/>
          <line x1="2" y1="13" x2="24" y2="13" stroke="#111" stroke-width="1.8"/>
          <line x1="4" y1="7.5" x2="22" y2="7.5" stroke="#111" stroke-width="1.5"/>
          <line x1="4" y1="18.5" x2="22" y2="18.5" stroke="#111" stroke-width="1.5"/>
        </svg>
      </div>
      <div class="web-band__url">WWW.<strong>RWHOLLIS</strong>.COM</div>
    </div>
  </section>

  <section class="card card--front" aria-label="Card front">
    <div class="front__brand"><span class="front__brand-name">RW HOLLIS</span></div>
    <div class="divider-blue"></div>
    <div class="divider-orange"></div>
    <div class="details-panel"></div>

    <div class="person">
      <div class="person__name">NAME <span>SURNAME</span></div>
      <div class="person__position">POSITION</div>
    </div>

    <ul class="contact">
      <li>Address. Building, City ZIP</li>
      <li><span class="contact__label">M:</span> 987 654322</li>
      <li><span class="contact__label">O:</span> 987 654 321</li>
      <li><span class="contact__label">E:</span> email@rwhollis.com</li>
    </ul>
  </section>

</div>
</body>
</html>
```